Business Card Design Project

Recently had a new logo made up for my company and new business cards done as well. I have attached the logos for your viewing. Additional projects may be needed. Good luck!

Industry/Entity Type

Business

```html
<!DOCTYPE html>
<html lang="en">
<head>
<meta charset="utf-8">
<title>Marlowe Financial Group – Business Card</title>
<link href="https://fonts.googleapis.com/css2?family=Bodoni+Moda:opsz,wght@6..96,400&display=swap" rel="stylesheet">
<style>
  :root {
    --navy: #161b28;
    --gold: #cdc77f;
    --paper: #ffffff;
    --ink: #111111;
  }
  * { margin: 0; padding: 0; box-sizing: border-box; }
  html, body { width: 776px; height: 1200px; overflow: hidden; background: var(--paper); }
  .card {
    position: relative;
    width: 776px;
    height: 1200px;
    background: var(--paper);
    font-family: "Bodoni Moda", serif;
    font-weight: 400;
    color: var(--ink);
    overflow: hidden;
  }
  .header-band {
    position: absolute;
    top: 0; left: 0;
    width: 776px;
    height: 257px;
    background: var(--navy);
    display: flex;
    align-items: center;
    justify-content: center;
  }
  .brand-name {
    color: var(--gold);
    font-size: 34px;
    font-weight: 400;
    letter-spacing: 3px;
    white-space: nowrap;
  }
  .identity {
    position: absolute;
    top: 345px;
    left: 0;
    width: 776px;
    text-align: center;
  }
  .person-name {
    font-size: 44px;
    font-weight: 400;
    line-height: 1;
  }
  .person-title {
    margin-top: 24px;
    font-size: 26px;
    line-height: 1;
  }
  .rule {
    position: absolute;
    top: 459px;
    left: 108px;
    width: 560px;
    height: 4px;
    background: var(--ink);
  }
  .contact, .address {
    position: absolute;
    left: 0;
    width: 776px;
    text-align: center;
    font-size: 32px;
    line-height: 46px;
  }
  .contact { top: 609px; }
  .address { top: 780px; }
  .wave {
    position: absolute;
    left: 0; top: 0;
    width: 776px;
    height: 1200px;
    pointer-events: none;
  }
</style>
</head>
<body>
  <div class="card">
    <header class="header-band">
      <div class="brand-name">MARLOWE FINANCIAL GROUP</div>
    </header>

    <section class="identity">
      <h1 class="person-name">Daniel R. Marlowe</h1>
      <p class="person-title">Estate Planning &amp; Insurance Specialist</p>
    </section>
    <div class="rule"></div>

    <section class="contact">
      <p>P: 516-555-0142 F: 516-555-0187</p>
      <p>Dmarlowe@marlowefinancial.com</p>
      <p>www.marlowefinancial.com</p>
    </section>

    <section class="address">
      <p>4200 Harbor Ridge Road, Suite 310E</p>
      <p>Westbury, New York 11590</p>
    </section>

    <svg class="wave" viewBox="0 0 776 1200" aria-hidden="true">
      <path fill="var(--gold)" d="M0,915 C150,905 320,930 460,1005 C505,1030 540,1070 562,1100 L0,1200 Z"/>
      <path fill="var(--navy)" d="M0,1023 C200,955 420,1040 560,1098 C650,1135 720,1160 776,1176 L776,1200 L0,1200 Z"/>
    </svg>
  </div>
</body>
</html>
```